Presentation Template for Copperline Ventures

We would like to have a template for our presentations since we have a new logo and want a new general image.

The new template should have as minimum Cover/Title Page, Bullets page and Regular page. We have a new logo and need the template to mach with it. For the bullets and regular page we want the design no take much part for including content, so we would like something that makes the slides look good but leaving most of room free for writing.

We would like the logo on the footer of the regular slides (not of course for the cover, dividers etc)

I'm attaching de logo here. Our logo colours are #b80016, #006ac6 and black

Thank you

Industry/Entity Type

It Company

Font styles to use
Other font styles liked:
• Maven Pro

Colors
ec1f27
0355a3
000000

Requirements
Must have
• Presentation template with Cover/Title Page, Bullets page and Regular page. Must match with our new logo.
• We would like the logo on the footer of the regular slides (not of course for the cover, dividers etc)
• Our logo colours are #b80016, #006ac6 and black
Nice to have
• Other type of slides, special bullets etc
Should not have
• I don't know

```html
<!DOCTYPE html>
<html lang="en">
<head>
<meta charset="utf-8">
<title>Copperline Ventures — Presentation Template</title>
<link href="https://fonts.googleapis.com/css2?family=Maven+Pro:wght@400;500;600;700&display=swap" rel="stylesheet">
<style>
:root{
  --navy:#072b4f;
  --red:#d51f28;
  --red-dark:#b80016;
  --blue:#0462c4;
  --blue-mid:#2b86e0;
  --blue-light:#9cc6ef;
  --ink:#1b1b1b;
  --grey:#7d7d7d;
  --white:#ffffff;
  --green:#6fc27a;
}
*{margin:0;padding:0;box-sizing:border-box}
html,body{width:1200px;height:1200px;overflow:hidden;background:var(--navy);font-family:"Maven Pro",sans-serif;color:var(--ink)}
.canvas{position:relative;width:1200px;height:1200px}
.slide{position:absolute;width:358px;height:202px;background:var(--white);overflow:hidden}
.c1{left:31px}.c2{left:421px}.c3{left:810px}
.r1{top:25px}.r2{top:262px}.r3{top:499px}.r4{top:737px}.r5{top:974px}
.abs{position:absolute}
.brand{position:absolute;display:flex;align-items:center;gap:3px;font-weight:700;font-size:5px;color:var(--red-dark);text-transform:uppercase;letter-spacing:.2px;line-height:1;white-space:nowrap}
.brand::before{content:"";width:8px;height:8px;background:var(--red-dark)}
.brand.light{color:var(--white)}
.brand.light::before{background:var(--white)}
.foot-brand{left:17px;bottom:10px}
.contact{position:absolute;right:17px;bottom:12px;font-size:4px;color:var(--ink);white-space:nowrap}
.contact b{font-weight:700}
.contact.light{color:var(--white)}
.num{position:absolute;top:17px;right:19px;width:7px;height:7px;background:var(--red-dark);color:#fff;font-size:4px;font-weight:700;display:flex;align-items:center;justify-content:center}
.hdr{position:absolute;left:18px;top:16px;font-size:9.5px;font-weight:600}
.subhdr-tiny{position:absolute;left:18px;font-size:3.5px;color:var(--grey);text-transform:uppercase}
.rule{position:absolute;left:0;top:34px;width:130px;height:1.5px;background:var(--red)}
.tiny{font-size:3.6px;line-height:1.55;color:var(--grey)}
.blue-t{color:var(--blue);font-weight:700;font-size:5px}
.photo{position:absolute}
.cover-top{position:absolute;left:0;top:0;width:100%;height:39px;background:#fff}
.cover-url{position:absolute;right:17px;top:17px;font-size:4px;color:var(--blue);font-weight:600;letter-spacing:.3px}
.cover-title{position:absolute;left:0;right:0;top:107px;text-align:center;color:#fff}
.cover-title .light{font-size:9px;font-weight:400}
.cover-title .strong{font-size:10px;font-weight:700;margin-top:3px}
ul.bullets{position:absolute;left:20px;top:80px;width:220px;list-style:none}
ul.bullets li{position:relative;padding-left:7px;margin-bottom:6px;font-size:3.6px;color:var(--ink);line-height:1.5}
ul.bullets li::before{content:"";position:absolute;left:0;top:1.6px;width:2px;height:2px;border-radius:50%;background:var(--ink)}
.panel-text{color:#fff}
.mission-h{font-size:8px;font-weight:700}
.green-rule{width:34px;height:1.2px;background:var(--green);margin:9px 0 8px}
.big-light{font-size:11.5px;font-weight:400;line-height:1.45}
.analysis{position:absolute;left:21px;width:130px;padding-left:5px;border-left:1px solid}
.analysis h4{font-size:5px;font-weight:700;margin-bottom:1px}
.tcard{position:absolute;background:var(--blue);color:#fff;font-size:3.6px;line-height:1.6;padding:13px 8px 6px;border-radius:2px}
.qmark{position:absolute;top:-5px;width:10px;height:10px;border-radius:50%;background:var(--red-dark);color:#fff;font-size:7px;font-weight:700;display:flex;align-items:center;justify-content:center;line-height:1}
.avatar{position:absolute;border-radius:50%;background:linear-gradient(#b9a89a,#4f4540)}
.pname{position:absolute;font-size:3.8px;font-weight:700;line-height:1.4;white-space:nowrap}
.pname span{display:block;font-weight:400;color:var(--grey);font-size:3px}
.member{position:absolute;top:79px;width:70px;text-align:center}
.member .avatar{position:relative;margin:0 auto;width:45px;height:45px}
.member h5{font-size:4.2px;font-weight:700;letter-spacing:.6px;margin-top:8px}
.member .role{font-size:3.6px;color:var(--grey);font-style:italic}
.member p{font-size:3px;color:var(--grey);line-height:1.5;margin-top:3px}
.center-h{position:absolute;left:0;right:0;text-align:center;font-weight:700;font-size:9px}
.center-p{position:absolute;left:90px;right:90px;text-align:center;font-size:3.8px;color:var(--grey);line-height:1.5}
.ring-label{position:absolute;width:70px;text-align:center;font-size:3.8px}
.ring-label b{display:block;font-weight:700;font-size:4px;color:var(--ink)}
.ring-label span{color:var(--grey);font-size:3.5px;line-height:1.5}
.ms{position:absolute;font-size:3.4px;color:var(--grey);line-height:1.5;width:70px}
.ms b{display:block;color:var(--red-dark);font-weight:600;font-size:5px}
</style>
</head>
<body>
<div class="canvas">

  <section class="slide c1 r1">
    <div class="photo" role="img" aria-label="Server room corridor with rows of racks" style="left:0;top:39px;width:100%;height:163px;background:radial-gradient(ellipse at 50% 45%,#6c6c6c 0%,#3a3a3a 45%,#141414 100%)"></div>
    <div class="cover-top"></div>
    <div class="brand" style="left:17px;top:16px">Copperline Ventures</div>
    <div class="cover-url">WWW.COPPERLINEVENTURES.COM</div>
    <div class="cover-title">
      <div class="light">Simple heading title</div>
      <div class="strong">Replace Header Title Here</div>
    </div>
  </section>

  <section class="slide c2 r1">
    <div class="hdr">Header text here</div>
    <div class="rule"></div>
    <div class="num">1</div>
    <div class="abs blue-t" style="left:20px;top:70px">Option sample here</div>
    <ul class="bullets">
      <li>Clear notes on the service plan, with room for a short second line of useful text here</li>
      <li>Short point on the plan</li>
      <li>Short point on the plan, with a note</li>
      <li>Short point on the plan, with a note</li>
    </ul>
    <div class="brand foot-brand">Copperline Ventures</div>
    <div class="contact">Phone: <b>+34 900-214-386</b> | Email: <b>hello@copperlineventures.com</b></div>
  </section>

  <section class="slide c3 r1">
    <div class="subhdr-tiny" style="top:9px">Sub heading</div>
    <div class="hdr" style="top:15px">Header text here</div>
    <div class="rule"></div>
    <div class="num">2</div>
    <div class="abs" style="left:18px;top:48px;width:290px">
      <div class="blue-t">Sub Header 2</div>
      <p class="tiny">Our team plans each project with care, from the first call to the final handover. We study your systems, map the risks and set clear goals so every step stays on track. Reports arrive each week and you always know who to call when a question comes up during the work.</p>
      <div class="blue-t" style="margin-top:8px">Sub Header 2</div>
      <p class="tiny">We build secure cloud setups that grow with your business. Each service is tested before launch and watched after it goes live. Our support staff answer fast, fix issues early and keep your data safe, so your people can focus on the work that matters most to your clients and partners every single day of the year.</p>
    </div>
    <div class="brand foot-brand">Copperline Ventures</div>
    <div class="contact">Phone: <b>+34 900-214-386</b> | Email: <b>hello@copperlineventures.com</b></div>
  </section>

  <section class="slide c1 r2" style="background:#f1f1f1">
    <div class="abs" style="inset:0 0 38px 0;background:#fff"></div>
    <div class="brand" style="left:17px;top:15px">Copperline Ventures</div>
    <div class="num">3</div>
    <div class="photo" role="img" aria-label="Network cables plugged into a switch, tinted blue" style="left:17px;top:39px;width:324px;height:134px;background:linear-gradient(100deg,#0462c4 0%,#0d63c0 45%,#3d7fc4 75%,#6a8db8 100%)"></div>
    <div class="abs panel-text" style="left:39px;top:62px">
      <div class="mission-h">Mission Statement</div>
      <div class="green-rule"></div>
      <div class="big-light">Helping exceptional<br>entrepreneurs grow<br>successful global businesses.</div>
    </div>
    <div class="contact" style="left:17px;right:auto;bottom:13px">Phone: <b>+34 900-214-386</b> | Email: <b>hello@copperlineventures.com</b></div>
  </section>

  <section class="slide c2 r2">
    <div class="hdr">Chart bar template</div>
    <div class="rule"></div>
    <div class="num">4</div>
    <div class="analysis" style="top:62px;border-color:var(--blue)"><h4 style="color:var(--blue)">Analysis one</h4><p class="tiny">We will show how you can add a query into your plan for each channel.</p></div>
    <div class="analysis" style="top:96px;border-color:var(--blue-mid)"><h4 style="color:var(--blue-mid)">Analysis Two</h4><p class="tiny">We will show how you can add a query into your plan for each channel.</p></div>
    <div class="analysis" style="top:129px;border-color:var(--red)"><h4 style="color:var(--red)">Analysis Three</h4><p class="tiny">We will show how you can add a query into your plan for each channel.</p></div>
    <svg class="abs" style="left:196px;top:48px" width="140" height="116" viewBox="0 0 140 116" font-family="Maven Pro, sans-serif" font-size="3.5" fill="#333">
      <g text-anchor="end">
        <text x="8" y="103">0</text><text x="8" y="91">1</text><text x="8" y="79">2</text><text x="8" y="67">3</text><text x="8" y="55">4</text><text x="8" y="43">5</text><text x="8" y="31">6</text><text x="8" y="19">7</text><text x="8" y="7">8</text>
      </g>
      <rect x="12" y="5" width="10" height="97" fill="#0462c4"/>
      <rect x="24" y="32" width="10" height="70" fill="#0462c4"/>
      <rect x="36" y="70" width="10" height="32" fill="#1a73cf"/>
      <rect x="48" y="24" width="10" height="78" fill="#3ea8ea"/>
      <rect x="60" y="80" width="10" height="22" fill="#5ab8ef"/>
      <rect x="72" y="44" width="10" height="58" fill="#e8353b"/>
      <rect x="84" y="36" width="10" height="66" fill="#e8353b"/>
      <rect x="96" y="53" width="10" height="49" fill="#ee5a5f"/>
      <g text-anchor="middle">
        <text x="17" y="110">1</text><text x="29" y="110">2</text><text x="41" y="110">3</text><text x="53" y="110">4</text><text x="65" y="110">5</text><text x="77" y="110">6</text><text x="89" y="110">7</text><text x="101" y="110">8</text><text x="113" y="110">9</text>
      </g>
    </svg>
    <div class="brand foot-brand">Copperline Ventures</div>
    <div class="contact">Phone: <b>+34 900-214-386</b> | Email: <b>hello@copperlineventures.com</b></div>
  </section>

  <section class="slide c3 r2">
    <div class="center-h" style="top:30px;font-weight:400;font-size:13px">Testimonials</div>
    <div class="num">5</div>
    <div class="tcard" style="left:50px;top:68px;width:80px;height:46px"><div class="qmark" style="left:10px">“</div>Great service from start to end, fast and clear work done.</div>
    <div class="tcard" style="left:139px;top:68px;width:80px;height:64px"><div class="qmark" style="left:10px">“</div>Great service from start to end. Fast, clear and kind work, done on time and on budget. Would hire again.</div>
    <div class="tcard" style="left:229px;top:68px;width:80px;height:46px"><div class="qmark" style="left:10px">“</div>Great service from start to end, fast and clear work.</div>
    <div class="avatar" role="img" aria-label="Client portrait" style="left:58px;top:123px;width:13px;height:13px"></div>
    <div class="pname" style="left:76px;top:125px">Hugo Lamar<span>Norbury Vale</span></div>
    <div class="avatar" role="img" aria-label="Client portrait" style="left:147px;top:143px;width:13px;height:13px"></div>
    <div class="pname" style="left:165px;top:145px">Felix Orton<span>Seychelles</span></div>
    <div class="avatar" role="img" aria-label="Client portrait" style="left:236px;top:123px;width:13px;height:13px"></div>
    <div class="pname" style="left:254px;top:125px">Nora Quill<span>Saint Vincent</span></div>
    <div class="brand foot-brand">Copperline Ventures</div>
    <div class="contact">Phone: <b>+34 900-214-386</b> | Email: <b>hello@copperlineventures.com</b></div>
  </section>

  <section class="slide c1 r3">
    <div class="photo" role="img" aria-label="Laptop on a desk showing a dashboard, tinted blue" style="left:0;top:0;width:100%;height:166px;background:linear-gradient(105deg,#0a4f9e 0%,#1464bf 40%,#4d87c4 70%,#8fa9c6 100%)"></div>
    <div class="abs" style="left:0;top:166px;width:100%;height:36px;background:#000"></div>
    <div class="abs panel-text" style="left:17px;top:45px">
      <div class="mission-h">Full image with text</div>
      <div class="green-rule" style="margin:7px 0 8px"></div>
      <div class="big-light">Helping exceptional<br>entrepreneurs grow<br>successful global businesses.</div>
    </div>
    <div class="brand light foot-brand" style="bottom:16px">Copperline Ventures</div>
    <div class="contact light" style="bottom:16px">Phone: <b>+34 900-214-386</b> | Email: <b>hello@copperlineventures.com</b></div>
  </section>

  <section class="slide c2 r3">
    <div class="subhdr-tiny" style="top:19px">Sub heading</div>
    <div class="hdr" style="top:24px">Meet Our Team</div>
    <div class="rule" style="top:41px"></div>
    <div class="num" style="top:19px">7</div>
    <p class="tiny abs" style="left:18px;top:52px;width:200px">Each member of our team brings years of hands-on work in cloud, data and security to every project.</p>
    <div class="member" style="left:24px"><div class="avatar" role="img" aria-label="Team member portrait"></div><h5>DARIO VENCE</h5><div class="role">Founder</div><p>Leads plans and keeps each project on time.</p></div>
    <div class="member" style="left:104px"><div class="avatar" role="img" aria-label="Team member portrait"></div><h5>OWEN REDDLE</h5><div class="role">Co-Founder</div><p>Builds cloud setups and guides new hires well.</p></div>
    <div class="member" style="left:184px"><div class="avatar" role="img" aria-label="Team member portrait"></div><h5>LINA CARROW</h5><div class="role">Co-Founder</div><p>Runs client care and weekly report work.</p></div>
    <div class="member" style="left:264px"><div class="avatar" role="img" aria-label="Team member portrait"></div><h5>RAVI DELMONT</h5><div class="role">Senior Advisor</div><p>Advises on security and long term growth.</p></div>
    <div class="brand foot-brand">Copperline Ventures</div>
    <div class="contact">Phone: <b>+34 900-214-386</b> | Email: <b>hello@copperlineventures.com</b></div>
  </section>

  <section class="slide c3 r3">
    <div class="subhdr-tiny" style="top:19px">Sub heading</div>
    <div class="hdr" style="top:24px">Header text here.</div>
    <div class="rule" style="top:41px"></div>
    <div class="num" style="top:19px">8</div>
    <div class="abs" style="left:18px;top:63px;width:125px">
      <div style="font-size:5px;font-weight:700">Sub Header 2</div>
      <p class="tiny">In this guide we show you how useful a query plan can be and why it should become a key part of your channel strategy. We will also show how you can add query work into your plan.</p>
      <p class="tiny" style="margin-top:6px">We will also show how you can add query work into your channel plan.</p>
    </div>
    <div class="photo" role="img" aria-label="Bright open office with long tables and black chairs" style="left:156px;top:49px;width:188px;height:119px;background:linear-gradient(180deg,#ecebe8 0%,#d9d6d1 55%,#5b5650 80%,#9a948d 100%)"></div>
    <div class="brand foot-brand">Copperline Ventures</div>
    <div class="contact">Phone: <b>+34 900-214-386</b> | Email: <b>hello@copperlineventures.com</b></div>
  </section>

  <section class="slide c1 r4">
    <div class="num">9</div>
    <div class="photo" role="img" aria-label="Desktop computer on a wooden desk with plants" style="left:17px;top:18px;width:268px;height:145px;background:linear-gradient(120deg,#d9d8d4 0%,#b9b6af 40%,#4a4743 60%,#a59f95 100%)"></div>
    <div class="abs panel-text" style="left:204px;top:82px;width:140px;height:63px;background:var(--blue);padding:11px 10px">
      <div style="font-size:5.5px;font-weight:700;margin-bottom:6px">Mission Statement</div>
      <div style="font-size:8.5px;line-height:1.45">Nobis videntur parum clari, fiant sollemnes in futurum.</div>
    </div>
    <div class="brand foot-brand">Copperline Ventures</div>
    <div class="contact">Phone: <b>+34 900-214-386</b> | Email: <b>hello@copperlineventures.com</b></div>
  </section>

  <section class="slide c2 r4">
    <div class="num">10</div>
    <div class="center-h" style="top:36px">Pie Chart Template</div>
    <p class="center-p" style="top:50px">Our results grow each year across every team and service we run for our clients.</p>
    <svg class="abs" style="left:0;top:0" width="358" height="202" viewBox="0 0 358 202" font-family="Maven Pro, sans-serif">
      <g fill="none" stroke-width="1">
        <circle cx="101" cy="104" r="20" stroke="#e3e3e3"/>
        <circle cx="101" cy="104" r="20" stroke="#0462c4" stroke-dasharray="94.2 125.7" transform="rotate(-90 101 104)"/>
        <circle cx="179" cy="104" r="20" stroke="#e3e3e3"/>
        <circle cx="179" cy="104" r="20" stroke="#0462c4" stroke-dasharray="44 125.7" transform="rotate(-90 179 104)"/>
        <circle cx="258" cy="104" r="20" stroke="#e3e3e3"/>
        <circle cx="258" cy="104" r="20" stroke="#0462c4" stroke-dasharray="94.2 125.7" transform="rotate(-90 258 104)"/>
      </g>
      <g font-size="9" font-weight="500" text-anchor="middle" fill="#1b1b1b">
        <text x="101" y="107">75%</text><text x="179" y="107">35%</text><text x="258" y="107">75%</text>
      </g>
    </svg>
    <div class="ring-label" style="left:66px;top:130px"><b>Analysis One</b><span>Hello everyone! Just a quick look at the project.</span></div>
    <div class="ring-label" style="left:144px;top:130px"><b>Analysis Two</b><span>Hello everyone! Just a quick look at the project.</span></div>
    <div class="ring-label" style="left:223px;top:130px"><b>Analysis Three</b><span>Hello everyone! Just a quick look at the project.</span></div>
    <div class="brand foot-brand">Copperline Ventures</div>
    <div class="contact">Phone: <b>+34 900-214-386</b> | Email: <b>hello@copperlineventures.com</b></div>
  </section>

  <section class="slide c3 r4">
    <div class="num">11</div>
    <div class="center-h" style="top:19px">Our Milestone</div>
    <p class="center-p" style="top:33px">Key steps on our path since the first office opened its doors to clients.</p>
    <div class="ms" style="left:72px;top:56px"><b>January 2012</b>Short note on this year of growth.</div>
    <div class="ms" style="left:146px;top:56px"><b>January 2014</b>Short note on this year of growth.</div>
    <div class="ms" style="left:219px;top:56px"><b>January 2016</b>Short note on this year of growth.</div>
    <svg class="abs" style="left:0;top:0" width="358" height="202" viewBox="0 0 358 202" font-family="Maven Pro, sans-serif">
      <g stroke="#7b9fd0" stroke-width=".6">
        <line x1="102" y1="81" x2="102" y2="88"/><line x1="175" y1="81" x2="175" y2="88"/><line x1="249" y1="81" x2="249" y2="88"/>
        <line x1="138" y1="146" x2="138" y2="153"/><line x1="212" y1="146" x2="212" y2="153"/>
      </g>
      <circle cx="102" cy="116" r="29" fill="#9cc6ef"/>
      <circle cx="138" cy="116" r="29" fill="#7eb3ea"/>
      <circle cx="175" cy="116" r="29" fill="#4c95e0"/>
      <circle cx="212" cy="116" r="29" fill="#2377d2"/>
      <circle cx="249" cy="116" r="29" fill="#0462c4"/>
      <g font-size="5" font-weight="600" fill="#fff" text-anchor="middle">
        <text x="100" y="118">2012</text><text x="138" y="118">2013</text><text x="175" y="118">2014</text><text x="212" y="118">2015</text><text x="251" y="118">2016</text>
      </g>
      <g fill="#b80016">
        <circle cx="119" cy="116" r="6"/><circle cx="156" cy="116" r="6"/><circle cx="193" cy="116" r="6"/><circle cx="230" cy="116" r="6"/>
      </g>
      <g fill="none" stroke="#fff" stroke-width="1">
        <polyline points="118,113.5 120.5,116 118,118.5"/><polyline points="155,113.5 157.5,116 155,118.5"/><polyline points="192,113.5 194.5,116 192,118.5"/><polyline points="229,113.5 231.5,116 229,118.5"/>
      </g>
    </svg>
    <div class="ms" style="left:117px;top:152px"><b>January 2013</b>Short note on this year of growth.</div>
    <div class="ms" style="left:190px;top:152px"><b>January 2015</b>Short note on this year of growth.</div>
    <div class="brand foot-brand">Copperline Ventures</div>
    <div class="contact">Phone: <b>+34 900-214-386</b> | Email: <b>hello@copperlineventures.com</b></div>
  </section>

  <section class="slide c1 r5">
    <div class="photo" role="img" aria-label="Bright meeting room with a dark table and white chairs" style="left:0;top:0;width:100%;height:100%;background:linear-gradient(180deg,#e9e8e6 0%,#dcdad6 50%,#3c3a38 72%,#cfccc7 100%)"></div>
    <div class="abs" style="left:0;top:168px;width:100%;height:34px;background:rgba(40,40,40,.78)"></div>
    <div class="num" style="background:transparent;border:.6px solid #fff;top:18px;right:14px">12</div>
    <div class="brand light foot-brand" style="bottom:14px">Copperline Ventures</div>
    <div class="contact light" style="bottom:14px">Phone: <b>+34 900-214-386</b> | Email: <b>hello@copperlineventures.com</b></div>
  </section>

  <section class="slide c2 r5" style="background:linear-gradient(180deg,#f6f7f9,#ffffff 60%,#f2f3f5)">
    <div class="brand" style="left:50%;transform:translateX(-50%);top:23px">Copperline Ventures</div>
    <div class="center-h" style="top:78px;font-weight:400;font-size:19px">Thank you</div>
    <div class="center-h" style="top:110px;font-size:3.8px;color:var(--blue);font-weight:600;letter-spacing:.3px">WWW.COPPERLINEVENTURES.COM</div>
    <div class="contact" style="left:0;right:0;text-align:center;bottom:10px">Phone: <b>+34 900-214-386</b> | Email: <b>hello@copperlineventures.com</b></div>
  </section>

</div>
</body>
</html>
```